Square graphic for social media post

I want to create a 1080 x 1080px all-black image for the quote below that I can share on social media. I want the emphasis to be primarily on the quote, secondarily on the portrait, and third (smallest) on the logo. I want the background on the portrait to be edited so it's transparent and just shows the face of the person on a black background (no brick wall visible).

Graphic color: black
Text color: white
Content: "What we went through is going to make the greatest generation of hoteliers our industry has ever seen." << biggest text
Dorian Welk << smaller text
President, Marrowgate Hotels << smaller text
[image of person - use whichever version looks better to you]
[Add Lodging Ledger logo - whichever looks better to you]

This image needs to be readable when sized down much smaller (400x400?) so want the text and portrait to take up most of the space.

I'd like the output both as PNG and original file (preferably Canva). Thanks!

Target Market(s)

Hotel managers

Industry/Entity Type

Hospitality

Font styles to use
Sans Serif

Colors

Designer to choose colors to be used in the design.

Requirements
Must have
• Needs to focus on the quote and the person quoted (the portrait)

```html
<!DOCTYPE html>
<html lang="en">
<head>
<meta charset="utf-8">
<title>Lodging Ledger – Quote Card</title>
<link href="https://fonts.googleapis.com/css2?family=Bebas+Neue&family=Great+Vibes&family=Oswald:wght@500&display=swap" rel="stylesheet">
<style>
  :root {
    --page: #ffffff;
    --card: #000000;
    --header-band: #262626;
    --accent-blue: #1c3475;
    --portrait-tone: #2b3558;
    --portrait-soft: #4a4a58;
    --ink: #ffffff;
  }
  html, body {
    margin: 0;
    width: 1200px;
    height: 1000px;
    overflow: hidden;
    background: var(--page);
  }
  .canvas {
    position: relative;
    width: 1200px;
    height: 1000px;
  }
  .quote-card {
    position: absolute;
    left: 283px;
    top: 183px;
    width: 634px;
    height: 634px;
    background: var(--card);
    overflow: hidden;
  }
  .accent-field {
    position: absolute;
    left: 0;
    top: 0;
    width: 320px;
    height: 634px;
    background: radial-gradient(ellipse 70% 60% at 35% 60%, var(--accent-blue) 0%, rgba(28, 52, 117, 0.35) 55%, rgba(0, 0, 0, 0) 100%);
  }
  .header-band {
    position: absolute;
    left: 30px;
    top: 7px;
    width: 604px;
    height: 105px;
    background: var(--header-band);
    display: flex;
    align-items: center;
    justify-content: center;
  }
  .brand-name {
    font-family: "Oswald", sans-serif;
    font-weight: 500;
    font-size: 11px;
    letter-spacing: 3px;
    color: var(--ink);
    margin: 0;
  }
  .portrait {
    position: absolute;
    left: 30px;
    top: 280px;
    width: 230px;
    height: 292px;
    background: linear-gradient(180deg, var(--portrait-soft) 0%, var(--portrait-tone) 100%);
  }
  .quote {
    position: absolute;
    right: 51px;
    top: 0;
    margin: 0;
    font-family: "Bebas Neue", sans-serif;
    font-weight: 400;
    color: var(--ink);
    text-align: right;
  }
  .quote-line {
    position: absolute;
    right: 0;
    white-space: nowrap;
    line-height: 1;
  }
  .quote-line--1 { top: 142px; font-size: 53px; }
  .quote-line--2 { top: 190px; font-size: 53px; }
  .quote-line--3 { top: 232px; font-size: 90px; }
  .quote-line--3 .lead-word { font-size: 49px; }
  .quote-line--4 { top: 302px; font-size: 90px; }
  .quote-line--5 { top: 380px; font-size: 53px; }
  .quote-line--6 { top: 424px; font-size: 53px; }
  .quote-line--7 { top: 468px; font-size: 53px; }
  .attribution {
    position: absolute;
    right: 0;
    top: 0;
    margin: 0;
    color: var(--ink);
  }
  .attribution-name,
  .attribution-role,
  .attribution-company {
    position: absolute;
    white-space: nowrap;
    line-height: 1;
  }
  .attribution-name {
    right: 55px;
    top: 531px;
    font-family: "Great Vibes", cursive;
    font-size: 21px;
  }
  .attribution-role,
  .attribution-company {
    right: 74px;
    font-family: "Oswald", sans-serif;
    font-weight: 500;
  }
  .attribution-role { top: 555px; font-size: 12px; }
  .attribution-company { top: 566px; font-size: 11px; }
</style>
</head>
<body>
<div class="canvas">
  <section class="quote-card">
    <div class="accent-field" role="img" aria-label="Decorative blue ribbon sweeping down the left side"></div>

    <header class="header-band">
      <p class="brand-name">LODGING LEDGER</p>
    </header>

    <div class="portrait" role="img" aria-label="Cut-out portrait of Dorian Welk on black"></div>

    <blockquote class="quote">
      <span class="quote-line quote-line--1">What we went through</span>
      <span class="quote-line quote-line--2">is going to make</span>
      <span class="quote-line quote-line--3"><span class="lead-word">The</span> greatest</span>
      <span class="quote-line quote-line--4">generation</span>
      <span class="quote-line quote-line--5">of hoteliers</span>
      <span class="quote-line quote-line--6">our industry</span>
      <span class="quote-line quote-line--7">has ever seen</span>
    </blockquote>

    <p class="attribution">
      <span class="attribution-name">Dorian Welk</span>
      <span class="attribution-role">PRESIDENT</span>
      <span class="attribution-company">MARROWGATE HOTELS</span>
    </p>
  </section>
</div>
</body>
</html>
```